ACV & Honey RTD

I need a label to go on our 250 ml bottle for our new ready-to-drink Apple Cider Vinegar and Honey drink.

Need a name that doesn't put the buyer off like "vinegar" does but still gives and idea of something a bit different "Elixir" with a bit of a bite' but very good for you

this is for export to Asia and is focused on the health, functional drink market

The logo is attached to this brief.

Would Honey & ACV R2D Work better for name

It looks like I can use the name "Plumvane Draught" now so I hope this clarifies the name issue, Sorry for this late change

Industry/Entity Type

Health

```html
<!DOCTYPE html>
<html lang="en">
<head>
<meta charset="utf-8">
<title>Plumvane Draught — Apple Cider Vinegar and Honey Drink Label</title>
<link rel="stylesheet" href="https://fonts.googleapis.com/css2?family=Varela+Round&family=Philosopher:wght@400;700&family=Cormorant+Garamond:ital,wght@0,500;1,500&display=swap">
<style>
  :root {
    --page-bg: #e9efea;
    --forest: #1f5a34;
    --forest-deep: #164a2a;
    --gold: #f5b94a;
    --gold-light: #f7d27a;
    --bronze: #a86f1f;
    --bronze-dark: #5e3a0c;
    --cream: #fff6c8;
    --honey: #e7b23c;
    --honey-deep: #c98f22;
    --foliage: #3f8a2e;
    --foliage-deep: #2a6424;
    --apple: #c9352a;
    --tagline: #f0d58a;
  }
  * { box-sizing: border-box; margin: 0; padding: 0; }
  html, body {
    width: 1200px;
    height: 855px;
    overflow: hidden;
    background: var(--page-bg);
  }
  .canvas {
    position: relative;
    width: 1200px;
    height: 855px;
  }
  .label {
    position: absolute;
    left: 395px;
    top: 150px;
    width: 410px;
    height: 556px;
    overflow: hidden;
    background: var(--forest);
    box-shadow: 0 6px 18px rgba(30, 60, 40, 0.18);
  }
  .label__artwork {
    position: absolute;
    left: 0;
    top: 56px;
    width: 410px;
    height: 390px;
    background:
      radial-gradient(ellipse 60% 45% at 50% 10%, var(--cream) 0%, var(--gold-light) 45%, rgba(231, 178, 60, 0) 100%),
      radial-gradient(ellipse 55% 40% at 30% 75%, rgba(201, 53, 42, 0.35) 0%, rgba(201, 53, 42, 0) 100%),
      radial-gradient(ellipse 55% 40% at 75% 65%, rgba(201, 53, 42, 0.3) 0%, rgba(201, 53, 42, 0) 100%),
      linear-gradient(180deg, var(--gold-light) 0%, var(--honey) 24%, var(--honey-deep) 34%, var(--foliage) 48%, var(--foliage-deep) 100%);
  }
  .label__wave {
    position: absolute;
    left: 0;
    top: 0;
    width: 410px;
    height: 120px;
  }
  .label__descriptor {
    position: absolute;
    left: 0;
    top: 10px;
    width: 410px;
    text-align: center;
    font-family: "Varela Round", sans-serif;
    font-size: 25px;
    line-height: 30px;
    color: var(--gold);
    text-shadow: 0 0 2px var(--bronze-dark), 1px 1px 0 var(--bronze-dark);
  }
  .label__name {
    position: absolute;
    left: 0;
    width: 410px;
    text-align: center;
    font-family: "Philosopher", sans-serif;
    font-weight: 700;
    color: var(--bronze);
    -webkit-text-stroke: 1.5px #fff6d8;
    text-shadow: 2px 3px 3px rgba(60, 35, 5, 0.5);
  }
  .label__name--first {
    top: 132px;
    font-size: 62px;
    line-height: 68px;
  }
  .label__name--second {
    top: 204px;
    font-size: 94px;
    line-height: 120px;
  }
  .label__footer {
    position: absolute;
    left: 0;
    bottom: 0;
    width: 410px;
    height: 110px;
    background: var(--forest-deep);
    padding-top: 26px;
    text-align: center;
    font-family: "Cormorant Garamond", serif;
    font-weight: 500;
    font-size: 23px;
    line-height: 27px;
    letter-spacing: 1px;
    color: var(--tagline);
  }
  .label__footer em { font-style: italic; letter-spacing: 0; }
</style>
</head>
<body>
<main class="canvas">
  <section class="label" aria-label="Plumvane Draught bottle label">
    <div class="label__artwork" role="img" aria-label="Illustration of golden honeycomb dripping honey over a leafy tree laden with red apples"></div>

    <svg class="label__wave" viewBox="0 0 410 120" aria-hidden="true">
      <path d="M0 0 H410 V78 C370 70 335 66 300 74 C255 84 225 102 190 100 C145 98 105 74 60 72 C35 71 15 75 0 79 Z" fill="var(--forest)"/>
      <path d="M0 79 C15 75 35 71 60 72 C105 74 145 98 190 100 C225 102 255 84 300 74 C335 66 370 70 410 78" fill="none" stroke="var(--gold-light)" stroke-width="3"/>
    </svg>

    <p class="label__descriptor">Apple Cider Vinegar<br>and Honey drink</p>

    <h1 class="label__name label__name--first">Plumvane</h1>
    <p class="label__name label__name--second">Draught</p>

    <p class="label__footer">MADE <em>with</em> PASSION<br><em>in</em> NEW ZEALAND</p>
  </section>
</main>
</body>
</html>
```